Chase The Copper Sun - This will be the titles of the podcast. The podcast is all about self developen

I need a graphic design for a podcast please. This podcast is all about heeling people make a change in their life Topics of business, health and fitness, learning, relationships. Pretty much anything to do with living a legendary life. I have not yet got a logo designed yet but will look at doing this in conjunction with this project.

Target Market(s)

20 - 35 year old males wanting to make a change in their lives and live a legendary life.

Industry/Entity Type

Life Coaching

Font styles to use
Sans Serif
Script

Colors
ffffff
000000
33a6d7

Requirements
Must have
• Simple bold great colours. Simplicity is key
Nice to have
• I have yet to form a logo so I may need one of those built too.
Should not have
• Open to suggestions just not too busy!

```html
<!DOCTYPE html>
<html lang="en">
<head>
<meta charset="utf-8">
<title>Chase The Copper Sun Podcast</title>
<link href="https://fonts.googleapis.com/css2?family=Cinzel:wght@500&family=Roboto+Condensed:wght@400&display=swap" rel="stylesheet">
<style>
  :root {
    --blue-deep: #0b6c99;
    --blue-mid: #1282b5;
    --blue-bright: #33a6d7;
    --ink: #000000;
    --ink-soft: #1f1f1f;
    --paper: #ffffff;
  }
  html, body {
    margin: 0;
    padding: 0;
    width: 1200px;
    height: 1200px;
    overflow: hidden;
    background: var(--blue-deep);
  }
  .cover {
    position: relative;
    width: 1200px;
    height: 1200px;
  }
  .cover-backdrop {
    position: absolute;
    inset: 0;
    background: radial-gradient(circle at 50% 50%, var(--blue-bright) 0%, var(--blue-mid) 45%, var(--blue-deep) 100%);
  }
  .cover-art {
    position: absolute;
    inset: 0;
    width: 1200px;
    height: 1200px;
  }
  .show-title {
    font-family: "Cinzel", "Trajan Pro", serif;
    font-weight: 500;
    fill: var(--paper);
    font-size: 158px;
  }
  .show-label {
    font-family: "Roboto Condensed", "Arial Narrow", sans-serif;
    fill: var(--paper);
    font-size: 44px;
  }
  .label-rule {
    stroke: var(--paper);
    stroke-width: 3;
  }
</style>
</head>
<body>
  <div class="cover">
    <div class="cover-backdrop" role="img" aria-label="Blue background with a halftone pattern of small diamonds"></div>
    <svg class="cover-art" viewBox="0 0 1200 1200" xmlns="http://www.w3.org/2000/svg">
      <defs>
        <linearGradient id="diamond-left" x1="0" y1="0" x2="0" y2="1">
          <stop offset="0" stop-color="#000000"/>
          <stop offset="1" stop-color="#1f1f1f"/>
        </linearGradient>
        <linearGradient id="diamond-right" x1="0" y1="0" x2="0" y2="1">
          <stop offset="0" stop-color="#1f1f1f"/>
          <stop offset="1" stop-color="#000000"/>
        </linearGradient>
      </defs>

      <g class="emblem">
        <polygon class="emblem-backing" points="614,72 1132,630 586,1136 66,576" fill="var(--paper)"/>
        <polygon class="emblem-frame" points="600,64 1140,602 600,1144 58,602" fill="var(--paper)"/>
        <polygon class="emblem-left" points="600,70 600,1138 64,602" fill="url(#diamond-left)"/>
        <polygon class="emblem-right" points="600,70 1134,602 600,1138" fill="url(#diamond-right)"/>
      </g>

      <text class="show-title" x="608" y="604" text-anchor="middle" textLength="780" lengthAdjust="spacingAndGlyphs">CHASE THE</text>
      <text class="show-title" x="608" y="736" text-anchor="middle" textLength="790" lengthAdjust="spacingAndGlyphs">COPPER SUN</text>

      <line class="label-rule" x1="420" y1="820" x2="478" y2="820"/>
      <text class="show-label" x="598" y="824" text-anchor="middle" textLength="228" lengthAdjust="spacing">PODCAST</text>
      <line class="label-rule" x1="718" y1="820" x2="774" y2="820"/>
    </svg>
  </div>
</body>
</html>
```